Cover for Every door Opens Where Every Door Opens

Book Cover Request
Format: Print and electronic (Quillmart)
Book Title: Every Door Opens Where Every Door Opens: Practical Roadmap for Courage and Progress
Author: R.K. Vantreel
Description: This self-help book, written by me, a self-proclaimed nobody, is filled with actionable insights and proven strategies that can help anyone. It combines humor with a serious undertone to deliver practical advice without the typical "self-helpy" vibe.
Catchphrase for the Cover: "Go from Oh Shit to Crushing It!" (or something similar)
Style: I want the cover to reflect my personality—funny, yet serious when needed. I'm open to suggestions and would love to see a design that captures the essence of the book without being too typical of the self-help genre.
Additional Information: I've attached a rough draft of the Quillmart description for more context.
Thank you for your help!
Target Market(s)
Anyone. but id say over 25
Requirements
Nice to have
- Honestly im really at a loss. Im hoping the description will help guide you. I gues i would like it to satand out of course. Be diffrent....but i know how crazy that sounds because everyone wants that. Just give me soem ideas!

```html
<!DOCTYPE html>
<html lang="en">
<head>
<meta charset="utf-8">
<title>Every Door Opens Where Every Door Opens — Book Cover</title>
<link rel="stylesheet" href="https://fonts.googleapis.com/css2?family=Archivo:wght@400;800;900&family=Bebas+Neue&display=swap">
<style>
  :root {
    --backdrop: #e1e1e1;
    --paper: #ffffff;
    --ink: #000000;
    --accent-red: #ec1c24;
    --art-light: #f7f3ea;
    --art-cool: #e4e9ef;
  }
  * { margin: 0; padding: 0; box-sizing: border-box; }
  html, body {
    width: 1200px;
    height: 1200px;
    overflow: hidden;
    background: var(--backdrop);
  }
  .book-cover {
    position: absolute;
    left: 240px;
    top: 60px;
    width: 720px;
    height: 1079px;
    background: var(--paper);
  }
  .tagline {
    position: absolute;
    top: 57px;
    left: 0;
    width: 100%;
    text-align: center;
    font-family: "Archivo", sans-serif;
    font-size: 30px;
    line-height: 36px;
    color: var(--ink);
    letter-spacing: -0.3px;
  }
  .tagline .tagline-top,
  .tagline .tagline-bottom { display: block; font-weight: 400; }
  .tagline .highlight { color: var(--accent-red); font-weight: 900; }
  .cover-artwork {
    position: absolute;
    left: 74px;
    top: 170px;
    width: 572px;
    height: 282px;
    background: linear-gradient(180deg, var(--art-light) 0%, var(--art-cool) 100%);
  }
  .title-block {
    position: absolute;
    left: 0;
    top: 0;
    width: 720px;
    height: 1079px;
    pointer-events: none;
  }
  .title-block text { font-family: "Bebas Neue", sans-serif; }
  .title-main { fill: var(--ink); }
  .title-accent { fill: var(--accent-red); }
  .title-connector { fill: var(--ink); }
  .connector-rule { fill: var(--ink); }
  .author-name {
    position: absolute;
    left: 0;
    top: 980px;
    width: 100%;
    text-align: center;
    font-family: "Archivo", sans-serif;
    font-weight: 900;
    font-size: 56px;
    line-height: 70px;
    color: var(--ink);
    letter-spacing: -1px;
  }
</style>
</head>
<body>
  <main class="book-cover">
    <p class="tagline">
      <span class="tagline-top">PRACTICAL ROADMAP FOR</span>
      <span class="tagline-bottom"><span class="highlight">COURAGE</span> AND <span class="highlight">PROGRESS</span></span>
    </p>

    <div class="cover-artwork" role="img" aria-label="Cover illustration: a balance scale holding two equal weights"></div>

    <svg class="title-block" viewBox="0 0 720 1079" aria-label="Every Door Opens Where Every Door Opens">
      <text class="title-main" x="86" y="635" font-size="212" textLength="548" lengthAdjust="spacingAndGlyphs">EVERY DOOR</text>
      <text class="title-accent" x="70" y="853" font-size="251" textLength="572" lengthAdjust="spacingAndGlyphs">OPENS</text>
      <rect class="connector-rule" x="73" y="874" width="97" height="3"/>
      <text class="title-connector" x="73" y="935" font-size="70" textLength="97" lengthAdjust="spacingAndGlyphs">WHERE</text>
      <rect class="connector-rule" x="73" y="941" width="97" height="3"/>
      <text class="title-accent" x="187" y="945" font-size="103" textLength="454" lengthAdjust="spacingAndGlyphs">EVERY DOOR OPENS</text>
    </svg>

    <p class="author-name">R.K. VANTREEL</p>
  </main>
</body>
</html>
```